Corporate Business Card

Very professional, Modern, Not to busy, include phone address email, website
(253) 555-0174, 61807 19th Street N, Kent, WA 98517, marcus@kestrelbayholding.com, brelvanindustries.com

Target Market(s)

Manufacturing

Industry/Entity Type

Aero, machining, manufacturing, Off road racing

Contact Information for Business Card

Phone, address email, website

```html
<!DOCTYPE html>
<html lang="en">
<head>
<meta charset="utf-8">
<title>Brelvan Industries — Business Card</title>
<link rel="stylesheet" href="https://fonts.googleapis.com/css2?family=Montserrat:wght@500;600;700&display=swap">
<style>
  :root {
    --navy: #15346b;
    --red: #d42a2f;
    --white: #ffffff;
    --ink: #1b1b1f;
    --silver: #c9cbd0;
    --stage: #e9eaed;
  }
  * { box-sizing: border-box; margin: 0; padding: 0; }
  html, body {
    width: 1200px; height: 927px; overflow: hidden;
    background: var(--stage);
    font-family: "Montserrat", Arial, sans-serif;
  }
  .card {
    position: absolute;
    left: 320px;
    width: 560px; height: 320px;
    border-radius: 26px;
    overflow: hidden;
    box-shadow: 0 10px 28px rgba(0,0,0,0.18);
  }
  .card--back { top: 90px; background: var(--navy); }
  .card--front { top: 510px; background: var(--white); }

  .brand-back {
    position: absolute; left: 0; right: 0; top: 118px;
    text-align: center;
    color: var(--silver);
    font-weight: 700;
    font-size: 44px;
    letter-spacing: 1px;
  }
  .rule-back {
    position: absolute; left: 130px; width: 300px; top: 196px;
    height: 3px; background: var(--silver);
  }

  .wave { position: absolute; inset: 0; width: 560px; height: 320px; }

  .brand-front {
    position: absolute; right: 36px; top: 38px;
    color: var(--navy);
    font-weight: 700;
    font-size: 28px;
    letter-spacing: 0.5px;
  }
  .rule-front {
    position: absolute; right: 120px; width: 230px; top: 86px;
    height: 2px; background: var(--navy);
  }

  .address {
    position: absolute; left: 40px; top: 92px;
    color: var(--ink);
    font-weight: 500; font-size: 14px; line-height: 1.45;
  }
  .contacts {
    position: absolute; left: 40px; top: 158px;
    list-style: none;
    color: var(--ink);
    font-weight: 500; font-size: 14px;
  }
  .contacts li { display: flex; align-items: center; gap: 10px; height: 23px; }
  .contacts svg { width: 15px; height: 15px; flex: none; }
</style>
</head>
<body>

<section class="card card--back" aria-label="Card back">
  <div class="brand-back">Brelvan Industries</div>
  <div class="rule-back"></div>
</section>

<section class="card card--front" aria-label="Card front">
  <svg class="wave" viewBox="0 0 560 320" aria-hidden="true">
    <path d="M0,304 C400,304 420,150 560,112 L560,320 L0,320 Z" fill="var(--navy)"/>
    <path d="M0,284 C400,284 420,130 540,100 C420,144 400,296 0,296 Z" fill="var(--red)"/>
  </svg>

  <div class="brand-front">Brelvan Industries</div>
  <div class="rule-front"></div>

  <p class="address">61807 19th Street N<br>Kent, WA 98517</p>

  <ul class="contacts">
    <li>
      <svg viewBox="0 0 16 16" aria-hidden="true"><path d="M4 1.5l2.2 2.6-1.3 1.6c.9 2 2.4 3.5 4.4 4.4l1.6-1.3 2.6 2.2-1.4 2.3C7 13 3 9 1.7 2.9z" fill="var(--red)"/></svg>
      (253) 555-0174
    </li>
    <li>
      <svg viewBox="0 0 16 16" aria-hidden="true"><rect x="1" y="3" width="14" height="10" rx="1" fill="var(--red)"/><path d="M1.5 3.5L8 9l6.5-5.5" stroke="#fff" stroke-width="1.3" fill="none"/></svg>
      marcus@kestrelbayholding.com
    </li>
    <li>
      <svg viewBox="0 0 16 16" aria-hidden="true"><circle cx="8" cy="8" r="7" fill="var(--red)"/><path d="M1 8h14M8 1c-3 3.5-3 10.5 0 14M8 1c3 3.5 3 10.5 0 14" stroke="#fff" stroke-width="1" fill="none"/></svg>
      www.brelvanindustries.com
    </li>
  </ul>
</section>

</body>
</html>
```